"Pause. Pivot. Prosper." Empowerment Book Cover

Hello, I need a hot, trendy, and contemporary book cover designed for my first book called "Pause. Pivot. Prosper. -- 365 Bold Confidence Notes for Anyone Seeking to Pause, Pivot, and Prosper Across Career & Personal Dreams."
This is my first book and I am really wanting to launch my brand with it... it would be awesome to match the inside/outside branding of the book. So we can either create the book cover to match the book guts, or update the book guts to match the cover.
Lastly, I just got a professional photoshoot done last week so we can use one of those images, or we can go with a different idea/style for the cover. The body of the book is attached. All questions welcomed, happy designing!
Target Market(s)
Gen Z, Millennials and Gen X.
Industry/Entity Type
Personal Development.
Requirements
Must have
- It must stand out and be different from other typical book covers.
Nice to have
- Success, Inspiration, Motivation, Mindset, Growth.
Should not have
- Clipart, stock art, stock look and feel.

```html
<!DOCTYPE html>
<html lang="en">
<head>
<meta charset="utf-8">
<title>Pause. Pivot. Prosper. — Cover Options</title>
<link href="https://fonts.googleapis.com/css2?family=Source+Sans+3:wght@300;400&display=swap" rel="stylesheet">
<style>
  :root {
    --page: #ffffff;
    --navy-deep: #0d1520;
    --band: #3a7c98;
    --initial-1: #8fb6dd;
    --initial-2: #1b80c6;
    --initial-3: #1a5cb5;
    --word-1: #dce9f2;
    --word-2: #62caec;
    --word-3: #19a7de;
    --subtitle: #5db6e2;
    --author: #6ec8ec;
  }
  html, body {
    margin: 0;
    width: 1200px;
    height: 849px;
    overflow: hidden;
    background: var(--page);
  }
  .sheet {
    position: relative;
    width: 1200px;
    height: 849px;
  }
  .cover {
    position: absolute;
    top: 31px;
    width: 529px;
    height: 786px;
    display: block;
  }
  .cover--wide { left: 63px; }
  .cover--close { left: 608px; }
  .cover text { font-family: "Source Sans 3", "Myriad Pro", sans-serif; }
  .bg { fill: var(--navy-deep); }
  .monogram { fill: var(--band); opacity: 0.4; font-weight: 400; font-size: 1250px; }
  .title { font-weight: 400; }
  .title .initial-1 { fill: var(--initial-1); }
  .title .initial-2 { fill: var(--initial-2); }
  .title .initial-3 { fill: var(--initial-3); }
  .title .word-1 { fill: var(--word-1); }
  .title .word-2 { fill: var(--word-2); }
  .title .word-3 { fill: var(--word-3); }
  .subtitle { fill: var(--subtitle); font-weight: 300; font-size: 17px; }
  .author { fill: var(--author); font-weight: 400; font-size: 60px; }
</style>
</head>
<body>
<div class="sheet">

  <svg class="cover cover--wide" viewBox="0 0 624 926" aria-label="Book cover, three-quarter portrait option">
    <defs>
      <radialGradient id="portrait-wide" cx="0.62" cy="0.42" r="0.6">
        <stop offset="0" stop-color="#3b4f78"/>
        <stop offset="0.45" stop-color="#22386a"/>
        <stop offset="1" stop-color="#0d1520" stop-opacity="0"/>
      </radialGradient>
    </defs>
    <rect class="bg" width="624" height="926"/>
    <rect x="120" y="20" width="504" height="906" fill="url(#portrait-wide)" role="img" aria-label="Photograph of the author in a navy suit, standing at three-quarter length"/>
    <text class="monogram" x="-70" y="900">P</text>
    <text class="title" x="57" y="453"><tspan class="initial-1" font-size="190">P</tspan><tspan class="word-1" font-size="112">ause.</tspan></text>
    <text class="title" x="45" y="571"><tspan class="initial-2" font-size="215">P</tspan><tspan class="word-2" font-size="122">ivot.</tspan></text>
    <text class="title" x="26" y="726"><tspan class="initial-3" font-size="285">P</tspan><tspan class="word-3" font-size="125">rosper.</tspan></text>
    <text class="subtitle" x="299" y="778">365 Bold Confidence Notes for Anyone</text>
    <text class="subtitle" x="299" y="801">Seeking to Pause, Pivot, and Prosper</text>
    <text class="subtitle" x="299" y="824">Across Career &amp; Personal Dreams.</text>
    <text class="author" x="311" y="893" text-anchor="middle">Daniel Okafor</text>
  </svg>

  <svg class="cover cover--close" viewBox="0 0 624 926" aria-label="Book cover, close portrait option">
    <defs>
      <radialGradient id="portrait-close" cx="0.66" cy="0.38" r="0.62">
        <stop offset="0" stop-color="#45577e"/>
        <stop offset="0.5" stop-color="#22386a"/>
        <stop offset="1" stop-color="#0d1520" stop-opacity="0"/>
      </radialGradient>
    </defs>
    <rect class="bg" width="624" height="926"/>
    <rect x="150" y="20" width="474" height="906" fill="url(#portrait-close)" role="img" aria-label="Close-up photograph of the author in a navy suit, head and shoulders"/>
    <text class="monogram" x="-70" y="900">P</text>
    <text class="title" x="57" y="453"><tspan class="initial-1" font-size="190">P</tspan><tspan class="word-1" font-size="112">ause.</tspan></text>
    <text class="title" x="45" y="571"><tspan class="initial-2" font-size="215">P</tspan><tspan class="word-2" font-size="122">ivot.</tspan></text>
    <text class="title" x="26" y="726"><tspan class="initial-3" font-size="285">P</tspan><tspan class="word-3" font-size="125">rosper.</tspan></text>
    <text class="subtitle" x="299" y="778">365 Bold Confidence Notes for Anyone</text>
    <text class="subtitle" x="299" y="801">Seeking to Pause, Pivot, and Prosper</text>
    <text class="subtitle" x="299" y="824">Across Career &amp; Personal Dreams.</text>
    <text class="author" x="311" y="893" text-anchor="middle">Daniel Okafor</text>
  </svg>

</div>
</body>
</html>
```